Bamboo Straw 4 Pack Cardboard Packaging

We would like a design with our logo and other bits of information for our 4 packs which will be in square cardboard packaging. We are all about the natural aspect of bamboo straws and saving our environment. Logos are attached as well as packaging option. The EXAMPLE there is not to be copied but used as inspiration. On the back of the package we will write our story.
Can use some of the facts below:
Bamboo is one most sustainable plants in the world! It can grow up to 1m in just 24 hours.
Bamboo is naturally anti- bacterial, anti fungal and odour resistant fibre
To grow Bamboo does not require fertiliser or any other harmful pesticides
Bamboo is a viable rep[lacement for wood. A Large tree can take over 35 years to mature, bamboo can take just 3, a single clump of bamboo can produce up to 15 kilometres of usable pole in its lifetime. It can out yield pine wood 6 to 1 in biomass production
It is the only plant left in the race to matching human consumption and deforestation one of its greatest qualities is after harvest its ability to renew growth is second to none
Bamboo straws are reusable and with care can last up to a year. They have anti bacterial qualitys due to an antimicrobial agent called bamboo kun found naturally living in the fibres
by using sustainable and reusable materials we are keeping tons and tons of garbage out of landfill. It was estimated in the USA nearly 500 million plastic straws are thrown into landfill every year, thats just the USA and just plastic straws.
Steel straws are great as they are reusable and also last a long period of time. Yet they still have an impact on the earth. You can’t obtain steel without mining the earth which we don’t need to get into the effects of.
Target Market(s)
Environmentally conscious consumers
Products will be sold online and in stores / Heath food stores
Requirements
Must have
- Only earthy colors (if any)
Nice to have
- We would like the packaging to be unique and a little cheeky. Talk about how bamboo straws are the best option.
- Have a “Check me out” or “take a look” arrow looking into the “window” where tot can see the straws.
- “Designed with love in Australia”
- “Australian owned”
- “Percentage of proceeds donated to ......(TBD)

```html
<!DOCTYPE html>
<html lang="en">
<head>
<meta charset="utf-8">
<title>Wattle Lane – Bamboo Drinking Straws Box</title>
<link rel="stylesheet" href="https://fonts.googleapis.com/css2?family=Amatic+SC:wght@400;700&family=Kaushan+Script&family=Montserrat:wght@400;500&display=swap">
<style>
  :root {
    --kraft: #c8a97a;
    --kraft-dark: #b8966a;
    --leaf: #648340;
    --leaf-text: #5f8a3a;
    --ink: #161514;
    --fold: #fbf7f0;
    --paper: #ffffff;
  }
  html, body {
    margin: 0;
    padding: 0;
    width: 1096px;
    height: 1200px;
    overflow: hidden;
    background: var(--paper);
  }
  .dieline {
    position: relative;
    width: 1096px;
    height: 1200px;
    font-family: "Montserrat", sans-serif;
    color: var(--ink);
  }
  .panel {
    position: absolute;
    background: var(--kraft);
    box-sizing: border-box;
    border: 1.5px solid var(--fold);
    box-shadow: 0 0 0 1px var(--kraft-dark);
  }
  .fold {
    position: absolute;
    left: 0;
    right: 0;
    height: 0;
    border-top: 1.5px solid var(--fold);
  }
  .fold-v {
    position: absolute;
    top: 0;
    bottom: 0;
    width: 0;
    border-left: 1.5px solid var(--fold);
  }

  /* side panels */
  .side { top: 112px; width: 97px; height: 964px; border-radius: 12px; }
  .side-left { left: 168px; }
  .side-right { left: 544px; }
  .side .fold:nth-of-type(1) { top: 97px; }
  .side .fold:nth-of-type(2) { top: 867px; }
  .side-dot {
    position: absolute;
    left: 33px;
    width: 27px;
    height: 27px;
    border-radius: 50%;
    background: var(--leaf);
  }
  .side-dot.top { top: 127px; }
  .side-dot.bottom { top: 797px; }
  .side-copy {
    position: absolute;
    left: 26px;
    top: 172px;
    margin: 0;
    writing-mode: vertical-rl;
    font-family: "Kaushan Script", cursive;
    font-size: 22px;
    line-height: 1;
    color: var(--leaf-text);
    white-space: nowrap;
  }
  .side-right .side-copy { top: 170px; font-size: 21.5px; }

  /* brand name */
  .brand {
    position: absolute;
    left: 0;
    right: 0;
    display: flex;
    justify-content: center;
    align-items: center;
    gap: 7px;
    font-family: "Montserrat", sans-serif;
    font-weight: 500;
    font-size: 21px;
    line-height: 1;
    color: var(--ink);
    white-space: nowrap;
  }
  .brand-dot {
    width: 12px;
    height: 12px;
    border-radius: 50%;
    background: var(--leaf);
  }

  /* front panel */
  .front {
    left: 262px;
    top: 66px;
    width: 287px;
    height: 1058px;
    border-radius: 14px;
    overflow: hidden;
  }
  .front .fold.lid-tuck { top: 51px; }
  .front .fold.lid-face { top: 143px; }
  .front .fold.base { top: 913px; }
  .front .fold.tuck-bottom { top: 1005px; }
  .lid-brand { top: 88px; transform: rotate(180deg); font-size: 15px; gap: 5px; }
  .lid-brand .brand-dot { width: 9px; height: 9px; }
  .front-brand { top: 204px; }
  .product-kicker {
    position: absolute;
    top: 284px;
    left: 0;
    right: 0;
    margin: 0;
    text-align: center;
    font-family: "Kaushan Script", cursive;
    font-size: 46px;
    line-height: 1;
    color: var(--leaf-text);
  }
  .product-name {
    position: absolute;
    top: 352px;
    left: 0;
    right: 0;
    margin: 0;
    text-align: center;
    font-family: "Amatic SC", sans-serif;
    font-weight: 700;
    font-size: 80px;
    line-height: 72px;
    color: var(--ink);
  }
  .window-art {
    position: absolute;
    left: 16px;
    top: 508px;
    width: 256px;
    height: 256px;
    border-radius: 50%;
    background: radial-gradient(circle, #b9996b 0 60%, #7fae4a 61% 70%, #9ec46b 76%, rgba(200,169,122,0) 100%);
  }
  .claims {
    position: absolute;
    left: 0;
    top: 780px;
    width: 100%;
    height: 290px;
    background: var(--leaf);
    font-family: "Amatic SC", sans-serif;
    color: var(--ink);
  }
  .claim {
    position: absolute;
    left: 25px;
    right: 25px;
    display: flex;
    justify-content: space-between;
    align-items: center;
    line-height: 1;
  }
  .claim.pack { top: 12px; font-size: 36px; font-weight: 400; letter-spacing: 1.5px; }
  .claim.love { top: 58px; font-size: 25px; }
  .claim.eco { top: 94px; font-size: 25px; }
  .claim-rule {
    position: absolute;
    left: 26px;
    right: 26px;
    border-top: 1.5px dotted var(--ink);
  }
  .claim-rule.first { top: 52px; }
  .claim-rule.second { top: 88px; }
  .heart { width: 18px; height: 16px; vertical-align: -2px; }

  /* back panel */
  .back {
    left: 638px;
    top: 206px;
    width: 333px;
    height: 777px;
    border-radius: 12px;
  }
  .back .fold-v { left: 278px; }
  .back-brand { top: 66px; width: 278px; }
  .facts-title {
    position: absolute;
    left: 28px;
    top: 162px;
    margin: 0;
    font-family: "Kaushan Script", cursive;
    font-weight: 400;
    font-size: 19px;
    color: var(--leaf-text);
  }
  .facts {
    position: absolute;
    left: 28px;
    top: 200px;
    width: 224px;
    margin: 0;
    padding: 0;
    list-style: none;
  }
  .fact {
    position: relative;
    padding-left: 26px;
    margin-bottom: 15px;
    font-size: 10.6px;
    line-height: 14.2px;
    text-align: justify;
  }
  .fact::before {
    content: "";
    position: absolute;
    left: 0;
    top: 2px;
    width: 18px;
    height: 18px;
    border-radius: 50%;
    background: var(--leaf);
  }
  .fact:nth-child(4) { margin-bottom: 18px; }
  .back-rule {
    position: absolute;
    left: 32px;
    top: 592px;
    width: 212px;
    border-top: 1.5px dashed var(--ink);
  }
  .care-note {
    position: absolute;
    left: 28px;
    top: 608px;
    width: 224px;
    margin: 0;
    text-align: center;
    font-family: "Amatic SC", sans-serif;
    font-weight: 700;
    font-size: 10px;
    line-height: 14px;
    text-transform: uppercase;
  }
  .label-space {
    position: absolute;
    left: 31px;
    top: 662px;
    width: 213px;
    height: 94px;
    background: var(--paper);
  }
</style>
</head>
<body>
<main class="dieline">

  <section class="panel side side-left">
    <span class="fold"></span><span class="fold"></span>
    <span class="side-dot top"></span>
    <p class="side-copy">Percentage of proceeds donated to ......</p>
    <span class="side-dot bottom"></span>
  </section>

  <section class="panel front">
    <span class="fold lid-tuck"></span>
    <span class="fold lid-face"></span>
    <div class="brand lid-brand"><span class="brand-dot"></span>Wattle Lane</div>
    <div class="brand front-brand"><span class="brand-dot"></span>Wattle Lane</div>
    <p class="product-kicker">Bamboo</p>
    <h1 class="product-name">DRINKING<br>STRAWS</h1>
    <div class="window-art" role="img" aria-label="Wreath of green bamboo stalks and leaves framing the see-through window onto the straws"></div>
    <div class="claims">
      <div class="claim pack"><span>4 PACK</span><span>•</span><span>STRAIGHT</span></div>
      <span class="claim-rule first"></span>
      <div class="claim love"><span>Designed with</span><svg class="heart" viewBox="0 0 20 18" aria-label="love"><path d="M10 17 C3 11 0 8 0 5 A5 5 0 0 1 10 3 A5 5 0 0 1 20 5 C20 8 17 11 10 17Z" fill="#161514"/></svg><span>in Australia</span></div>
      <span class="claim-rule second"></span>
      <div class="claim eco"><span>Biodegradable</span><span>•</span><span>Sustainable</span></div>
    </div>
    <span class="fold base"></span>
    <span class="fold tuck-bottom"></span>
  </section>

  <section class="panel side side-right">
    <span class="fold"></span><span class="fold"></span>
    <span class="side-dot top"></span>
    <p class="side-copy">Bamboo straws are reusable and with care can last up to a year.</p>
    <span class="side-dot bottom"></span>
  </section>

  <section class="panel back">
    <span class="fold-v"></span>
    <div class="brand back-brand"><span class="brand-dot"></span>Wattle Lane</div>
    <h2 class="facts-title">Bamboo Facts:</h2>
    <ul class="facts">
      <li class="fact">Bamboo is one most sustainable plants in the world! It can grow up to 1m in just 24 hours.</li>
      <li class="fact">Bamboo is naturally anti-bacterial, anti fungal and odour resistant fibre.</li>
      <li class="fact">To grow Bamboo does not require fertiliser or any other harmful pesticides.</li>
      <li class="fact">Bamboo is a viable replacement for wood. A Large tree can take over 35 years to mature, bamboo can take just 3, a single clump of bamboo can produce up to 15 kilometres of usable pole in its lifetime. It can out yield pine wood 6 to 1 in biomass production.</li>
      <li class="fact">It is the only plant left in the race to matching human consumption and deforestation one of its greatest qualities is after harvest its ability to renew growth is second to none.</li>
    </ul>
    <span class="back-rule"></span>
    <p class="care-note">Reuse your straws, rinse after every drink,<br>and let them dry upright in open air.</p>
    <div class="label-space"></div>
  </section>

</main>
</body>
</html>
```